Environmentally conscious Waste Management Company requires business card

We Require a Business card for our environmentally conscious waste management company . The business card should have a very clean design. be double sided and incorporate our logo..
The card will need o have 9 lines for the contact details - that are
Name
Title
Business
Address Line 1
Address Line 2
Address Line 3
Phone
Mobile
Email

Industry/Entity Type

Waste Management

Font styles to use
Other font styles liked:
• Helvetica or similar

```html
<!DOCTYPE html>
<html lang="en">
<head>
<meta charset="utf-8">
<title>Brightloop business card</title>
<link rel="stylesheet" href="https://fonts.googleapis.com/css2?family=Lato:wght@400;700&display=swap">
<style>
  :root {
    --green: #3db54a;
    --card-black: #1c1c1c;
    --white: #ffffff;
    --text-light: #e6e6e6;
    --page: #ecebe8;
  }
  * { box-sizing: border-box; margin: 0; padding: 0; }
  html, body {
    width: 1200px; height: 1000px; overflow: hidden;
    background: var(--page);
    font-family: "Lato", Helvetica, Arial, sans-serif;
  }
  .sheet {
    width: 1200px; height: 1000px;
    display: flex; flex-direction: column;
    align-items: center; justify-content: center; gap: 48px;
  }
  .card {
    width: 720px; height: 420px;
    border-radius: 22px; overflow: hidden; position: relative;
    box-shadow: 0 6px 18px rgba(0,0,0,0.18);
  }

  /* front side */
  .card--front {
    background: var(--card-black);
    display: flex; align-items: center; justify-content: center;
  }
  .card--front .brand-name {
    color: var(--white); font-size: 64px; font-weight: 700;
    letter-spacing: 6px; line-height: 1; white-space: nowrap;
  }

  /* back side */
  .card--back { background: var(--card-black); }
  .back-top {
    position: absolute; left: 0; top: 0; width: 100%; height: 150px;
    background: var(--white);
  }
  .back-top .brand-name {
    position: absolute; left: 44px; top: 52px;
    color: var(--card-black); font-size: 40px; font-weight: 700;
    letter-spacing: 4px; line-height: 1; white-space: nowrap;
  }
  .back-stripe {
    position: absolute; left: 0; top: 150px; width: 100%; height: 11px;
    background: var(--green);
  }

  .person { position: absolute; left: 44px; top: 198px; }
  .person-name { color: var(--green); font-size: 22px; font-weight: 700; letter-spacing: 0.3px; }
  .person-title { color: var(--text-light); font-size: 17px; margin-top: 2px; }

  .contact-list { position: absolute; left: 44px; top: 286px; list-style: none; }
  .contact-list li {
    display: flex; align-items: center; gap: 14px;
    color: var(--text-light); font-size: 17px; height: 26px;
  }
  .contact-list svg { width: 18px; height: 18px; fill: var(--green); flex: none; }

  .company { position: absolute; left: 470px; top: 294px; }
  .company-name { color: var(--green); font-size: 17px; font-weight: 700; letter-spacing: 0.3px; }
  .company-address { color: var(--text-light); font-size: 17px; line-height: 25px; margin-top: 2px; }
</style>
</head>
<body>
<main class="sheet">

  <section class="card card--front" aria-label="Card front">
    <span class="brand-name">BRIGHTLOOP</span>
  </section>

  <section class="card card--back" aria-label="Card back">
    <div class="back-top">
      <span class="brand-name">BRIGHTLOOP</span>
    </div>
    <div class="back-stripe"></div>

    <div class="person">
      <p class="person-name">YOUR NAME</p>
      <p class="person-title">Director</p>
    </div>

    <ul class="contact-list">
      <li>
        <svg viewBox="0 0 24 24" aria-hidden="true"><path d="M6.6 10.8a15.1 15.1 0 0 0 6.6 6.6l2.2-2.2c.3-.3.7-.4 1-.2 1.1.4 2.3.6 3.6.6.6 0 1 .4 1 1V20c0 .6-.4 1-1 1A17 17 0 0 1 3 4c0-.6.4-1 1-1h3.5c.6 0 1 .4 1 1 0 1.3.2 2.5.6 3.6.1.3 0 .7-.2 1z"/></svg>
        <span>+101 555 204 318</span>
      </li>
      <li>
        <svg viewBox="0 0 24 24" aria-hidden="true"><path d="M7 1h10a2 2 0 0 1 2 2v18a2 2 0 0 1-2 2H7a2 2 0 0 1-2-2V3a2 2 0 0 1 2-2zm0 4v12h10V5zm5 14a1.2 1.2 0 1 0 0 2.4A1.2 1.2 0 0 0 12 19z"/></svg>
        <span>+101 555 204 318</span>
      </li>
      <li>
        <svg viewBox="0 0 24 24" aria-hidden="true"><path d="M2 5h20v2l-10 6L2 7zm0 4.3l10 6 10-6V19H2z"/></svg>
        <span>name@brightloop.com.au</span>
      </li>
    </ul>

    <div class="company">
      <p class="company-name">BRIGHTLOOP</p>
      <p class="company-address">Suite 1, Name of Street,<br>Road, City, Country 12345</p>
    </div>
  </section>

</main>
</body>
</html>
```